Busy Pelicans Bag Tags -Business Card to be used as Bag Tags

No company logo yet
Memory bag tags (or 'busy p-tags' / e for elephant) for primary school children (kindergarten - grade 6) to help reduce lost property. Side 1 of card A simple picture of school hat, lunch box and water bottle with a tick or gold star next to it to prompt them to keep their belongings in bag.
Side 2 of card a statement ie AVOID Lost Property Keep it in your Bag or Don't Leave It Behind with an image of an elephants behind (kids style).
Bright , fun and simple.
Inspiration Harriet and Moss style.
Leave room for hole punch in centre or at side.

Target Market(s)

school children

Industry/Entity Type

School

Contact Information for Business Card

busy.pelicans@mailnest.com.au

Requirements
Must have
• a kid friendly elephant design
Nice to have
• bright friendly and clear
• child friendly
Should not have
• no adult themes

```html
<!DOCTYPE html>
<html lang="en">
<head>
<meta charset="utf-8">
<title>Busy Pelicans Bag Tags</title>
<link rel="stylesheet" href="https://fonts.googleapis.com/css2?family=Didact+Gothic&family=Patrick+Hand&display=swap">
<style>
  :root {
    --page: #ffffff;
    --tag-front: #e8536a;
    --tag-back: #cdd63f;
    --hole: #ffffff;
    --label: #ffffff;
    --star: #fbb040;
    --star-edge: #f7d27a;
    --ink: #1d2b4f;
    --bubble: #ffffff;
    --hat: #b5a88a;
    --hat-shade: #8d8368;
    --lunchbox: #a9c95a;
    --lunchbox-lid: #f4f1e4;
    --bottle: #cfe6f5;
    --bottle-label: #2f6fb8;
    --elephant: #aaa49c;
    --elephant-shade: #8f8a83;
  }
  * { margin: 0; padding: 0; box-sizing: border-box; }
  html, body { width: 1200px; height: 927px; overflow: hidden; background: var(--page); }
  .canvas { position: relative; width: 1200px; height: 927px; }

  .tag { position: absolute; border-radius: 26px; }
  .tag--checklist { left: 123px; top: 76px; width: 385px; height: 672px; background: var(--tag-front); }
  .tag--message { left: 576px; top: 78px; width: 384px; height: 674px; background: var(--tag-back); }

  .punch-hole { position: absolute; top: 12px; left: 50%; width: 48px; height: 48px; margin-left: -24px; border-radius: 50%; background: var(--hole); }

  .item-art { position: absolute; }
  .item-art--hat {
    left: 20px; top: 61px; width: 162px; height: 131px;
    background: linear-gradient(180deg, var(--hat) 0 60%, var(--hat-shade) 60% 72%, transparent 72%);
    border-radius: 45% 45% 12px 12px / 60% 60% 12px 12px;
  }
  .item-art--lunchbox {
    left: 19px; top: 254px; width: 170px; height: 160px;
    background: linear-gradient(180deg, var(--lunchbox-lid) 0 42%, var(--lunchbox) 42%);
    border-radius: 10px;
  }
  .item-art--bottle {
    left: 60px; top: 469px; width: 67px; height: 152px;
    background: linear-gradient(180deg, var(--bottle) 0 40%, var(--bottle-label) 40% 62%, var(--bottle) 62%);
    border-radius: 22px 22px 14px 14px;
  }

  .item-label {
    position: absolute; left: 0; width: 200px; text-align: center;
    font-family: "Patrick Hand", cursive; font-size: 27px; color: var(--label);
    text-transform: uppercase; line-height: 1;
  }
  .item-label--hat { top: 200px; }
  .item-label--lunchbox { top: 416px; }
  .item-label--bottle { top: 624px; }

  .gold-star { position: absolute; width: 82px; height: 80px; }
  .gold-star--hat { left: 250px; top: 78px; }
  .gold-star--lunchbox { left: 258px; top: 298px; }
  .gold-star--bottle { left: 256px; top: 514px; }

  .message-bubble {
    position: absolute; left: 8px; top: 194px; width: 370px; height: 200px;
    border-radius: 50%; background: var(--bubble);
  }
  .message-text {
    position: absolute; left: 0; width: 100%; text-align: center;
    font-family: "Didact Gothic", sans-serif; color: var(--ink);
  }
  .message-text--lead { top: 205px; font-size: 54px; line-height: 56px; letter-spacing: 2px; }
  .message-text--body { top: 262px; font-size: 40px; line-height: 44px; letter-spacing: 2px; }

  .elephant-art {
    position: absolute; left: 24px; top: 427px; width: 312px; height: 203px;
    background: radial-gradient(ellipse at 55% 45%, var(--elephant) 60%, var(--elephant-shade));
    border-radius: 30% 45% 16px 16px / 40% 55% 16px 16px;
  }

  .contact-email {
    position: absolute; left: 0; top: 640px; width: 100%; text-align: center;
    font-family: "Didact Gothic", sans-serif; font-size: 17px; color: var(--ink);
  }
</style>
</head>
<body>
<main class="canvas">
  <section class="tag tag--checklist">
    <span class="punch-hole"></span>

    <div class="item-art item-art--hat" role="img" aria-label="Illustration of a khaki school bucket hat"></div>
    <p class="item-label item-label--hat">School Hat</p>
    <svg class="gold-star gold-star--hat" viewBox="0 0 82 80" aria-hidden="true"><polygon points="41,3 51,29 79,30 57,48 65,76 41,60 17,76 25,48 3,30 31,29" fill="var(--star)" stroke="var(--star-edge)" stroke-width="2" stroke-linejoin="round"/></svg>

    <div class="item-art item-art--lunchbox" role="img" aria-label="Illustration of an open green lunch box with a brown handle"></div>
    <p class="item-label item-label--lunchbox">Lunch Box</p>
    <svg class="gold-star gold-star--lunchbox" viewBox="0 0 82 80" aria-hidden="true"><polygon points="41,3 51,29 79,30 57,48 65,76 41,60 17,76 25,48 3,30 31,29" fill="var(--star)" stroke="var(--star-edge)" stroke-width="2" stroke-linejoin="round"/></svg>

    <div class="item-art item-art--bottle" role="img" aria-label="Illustration of a plastic water bottle with a blue label"></div>
    <p class="item-label item-label--bottle">Water Bottle</p>
    <svg class="gold-star gold-star--bottle" viewBox="0 0 82 80" aria-hidden="true"><polygon points="41,3 51,29 79,30 57,48 65,76 41,60 17,76 25,48 3,30 31,29" fill="var(--star)" stroke="var(--star-edge)" stroke-width="2" stroke-linejoin="round"/></svg>
  </section>

  <section class="tag tag--message">
    <span class="punch-hole"></span>

    <div class="message-bubble"></div>
    <p class="message-text message-text--lead">AVOID</p>
    <p class="message-text message-text--body">Lost Property<br>Keep it in your<br>Bag Please!</p>

    <div class="elephant-art" role="img" aria-label="Child-style sketch of a grey elephant seen from the side, tail showing"></div>

    <p class="contact-email">busy.pelicans@mailnest.com.au</p>
  </section>
</main>
</body>
</html>
```